Meridian Groundworks
Project: Construction Stationery
Construction Stationery - Construction
Construction Stationery
Professional
Eng. Samir Qutub
Construction Manager
P.O.Box: 4706 Jeddah 23857 Palm Orchard Street Saudi Arabia Phone: +966 12 4870391 info@meridiangroundworks.example
info@meridiangroundworks.example
www.meridiangroundworks.example
Please don't submit business card solo, submit the following at once:- 1. Business card 2. Letterhead A 3. Letterhead B 4. Envelope 5. Notepad 6. Folder
Design
kelvorunt kelvorunt
Please don't submit business card solo, I don't need all stationery i need only what's mentioned in additional comments section in the brief. Please check attached logo.

```html
<!DOCTYPE html>
<html lang="en">
<head>
<meta charset="utf-8">
<title>Meridian Groundworks — Construction Stationery</title>
<link href="https://fonts.googleapis.com/css2?family=Montserrat:wght@400;600;800&display=swap" rel="stylesheet">
<style>
  :root{
    --bg:#e9eaec;
    --paper:#ffffff;
    --navy:#1f3f9c;
    --blue:#2d5fd6;
    --orange:#f39a1f;
    --ink:#4a4f5a;
    --muted:#8a8f99;
  }
  *{box-sizing:border-box;margin:0;padding:0}
  html,body{width:1200px;height:936px;overflow:hidden}
  body{background:var(--bg);font-family:"Montserrat",sans-serif;color:var(--ink);position:relative}
  .sheet{position:absolute;background:var(--paper);overflow:hidden;box-shadow:0 2px 6px rgba(0,0,0,.12)}
  .brand{font-weight:800;color:var(--navy);text-transform:uppercase;letter-spacing:.5px;display:flex;align-items:center;gap:6px;line-height:1}
  .brand .dot{width:.9em;height:.9em;border-radius:50%;background:var(--orange);flex:none}
  .wave{position:absolute;left:0;bottom:0;width:100%}
  .url{position:absolute;left:0;right:0;text-align:center;color:#fff;font-weight:600;letter-spacing:2px}

  /* Letterhead */
  .letterhead{left:185px;top:51px;width:414px;height:558px}
  .letterhead .brand{position:absolute;left:22px;top:28px;font-size:12px}
  .contact{position:absolute;right:22px;top:24px;list-style:none;font-size:5.2px;line-height:9px;text-align:right;color:var(--muted)}
  .contact li::after{content:"";display:inline-block;width:4px;height:4px;background:var(--orange);margin-left:4px;vertical-align:middle}
  .letter{position:absolute;left:22px;top:118px;width:300px;font-size:5.6px;line-height:8.4px}
  .letter p{margin-bottom:8px}
  .letter .sign{margin-top:18px;font-weight:600;color:var(--navy)}
  .letter .sign span{font-weight:400;color:var(--muted)}
  .letterhead .url{bottom:12px;font-size:7px}

  /* Folder */
  .folder{left:634px;top:51px;width:457px;height:563px}
  .folder .brand{position:absolute;left:0;right:0;top:300px;justify-content:center;font-size:24px}
  .folder .url{bottom:14px;font-size:8px}

  /* Business cards */
  .card{width:203px;height:109px}
  .card-front{left:46px;top:644px}
  .card-back{left:46px;top:771px}
  .card .brand{position:absolute}
  .card-front .brand{left:10px;top:20px;font-size:6px;gap:4px}
  .card-front .brand .name{display:block;line-height:1.15}
  .card-back .brand{left:14px;top:40px;font-size:7px}
  .card .person{position:absolute;left:104px;top:14px;width:94px;font-size:4.5px;line-height:6.6px;color:var(--muted);white-space:nowrap}
  .card .person strong{color:var(--orange);font-weight:600;display:block;font-size:5.2px}

  /* Envelopes */
  .envelope{left:264px;top:660px;width:441px;height:215px}
  .envelope .brand{position:absolute;left:16px;top:22px;font-size:12px}
  .envelope-back{left:736px;top:665px;width:429px;height:220px}
  .envelope-back .url{top:24px;font-size:8px}
</style>
</head>
<body>

<section class="sheet letterhead" aria-label="Letterhead">
  <div class="brand"><span class="dot"></span>Meridian Groundworks</div>
  <ul class="contact">
    <li>P.O.Box: 4706 Jeddah 23857</li>
    <li>Palm Orchard Street, Saudi Arabia</li>
    <li>Phone: +966 12 4870391</li>
    <li>info@meridiangroundworks.example</li>
    <li>www.meridiangroundworks.example</li>
  </ul>
  <div class="letter">
    <p>June 12, 2024</p>
    <p>Dear Client,<br>Project Office, Jeddah Site</p>
    <p>Thank you for choosing our team for the foundation works on your new building. We have reviewed the soil report and prepared a full schedule for piling, excavation and concrete works.</p>
    <p>Our engineers will be on site from the first week of next month. Safety plans and method statements are attached for your review.</p>
    <p>Please contact our office with any questions about the programme or the attached drawings.</p>
    <p>Best regards,</p>
    <p class="sign">Eng. Samir Qutub<br><span>Construction Manager</span></p>
  </div>
  <svg class="wave" viewBox="0 0 414 80" height="80" preserveAspectRatio="none" aria-hidden="true">
    <path d="M0 40 Q200 64 414 18 L414 26 Q200 70 0 46Z" fill="var(--orange)"/>
    <path d="M0 48 Q200 72 414 28 L414 80 L0 80Z" fill="var(--blue)"/>
    <path d="M0 60 Q220 80 414 40 L414 80 L0 80Z" fill="var(--navy)" opacity=".55"/>
  </svg>
  <div class="url">www.meridiangroundworks.example</div>
</section>

<section class="sheet folder" aria-label="Presentation folder">
  <div class="brand"><span class="dot"></span>Meridian Groundworks</div>
  <svg class="wave" viewBox="0 0 457 110" height="110" preserveAspectRatio="none" aria-hidden="true">
    <path d="M0 56 Q220 88 457 20 L457 30 Q220 96 0 64Z" fill="var(--orange)"/>
    <path d="M0 66 Q220 98 457 32 L457 110 L0 110Z" fill="var(--blue)"/>
    <path d="M0 82 Q240 108 457 56 L457 110 L0 110Z" fill="var(--navy)" opacity=".55"/>
  </svg>
  <div class="url">www.meridiangroundworks.example</div>
</section>

<section class="sheet card card-front" aria-label="Business card front">
  <div class="brand"><span class="dot"></span><span class="name">Meridian<br>Groundworks</span></div>
  <div class="person">
    <strong>Eng. Samir Qutub</strong>
    Construction Manager<br>
    +966 12 4870391<br>
    P.O.Box: 4706 Jeddah 23857<br>
    info@meridiangroundworks.example
  </div>
  <svg class="wave" viewBox="0 0 203 26" height="26" preserveAspectRatio="none" aria-hidden="true">
    <path d="M0 14 Q100 24 203 4 L203 8 Q100 27 0 17Z" fill="var(--orange)"/>
    <path d="M0 18 Q100 28 203 10 L203 26 L0 26Z" fill="var(--blue)"/>
  </svg>
</section>

<section class="sheet card card-back" aria-label="Business card back">
  <div class="brand"><span class="dot"></span>Meridian Groundworks</div>
  <svg class="wave" viewBox="0 0 203 22" height="22" preserveAspectRatio="none" aria-hidden="true">
    <path d="M0 12 Q100 20 203 4 L203 7 Q100 23 0 15Z" fill="var(--orange)"/>
    <path d="M0 16 Q100 24 203 9 L203 22 L0 22Z" fill="var(--blue)"/>
  </svg>
</section>

<section class="sheet envelope" aria-label="Envelope front">
  <div class="brand"><span class="dot"></span>Meridian Groundworks</div>
  <svg class="wave" viewBox="0 0 441 60" height="60" preserveAspectRatio="none" aria-hidden="true">
    <path d="M0 30 Q220 52 441 10 L441 17 Q220 58 0 36Z" fill="var(--orange)"/>
    <path d="M0 38 Q220 60 441 20 L441 60 L0 60Z" fill="var(--blue)"/>
    <path d="M0 50 Q240 64 441 36 L441 60 L0 60Z" fill="var(--navy)" opacity=".55"/>
  </svg>
</section>

<section class="sheet envelope-back" aria-label="Envelope back">
  <svg viewBox="0 0 429 220" width="429" height="220" style="position:absolute;left:0;top:0" aria-hidden="true">
    <path d="M0 0 L429 0 L429 70 Q215 40 0 118Z" fill="var(--blue)"/>
    <path d="M0 118 Q215 40 429 70 L429 76 Q215 48 0 124Z" fill="var(--orange)"/>
    <path d="M0 124 Q215 48 429 76 L429 80 Q215 54 0 128Z" fill="#dfe3ea"/>
  </svg>
  <div class="url">www.meridiangroundworks.example</div>
</section>

</body>
</html>
```